Korbin Ventilation's. "We're Dalton beyond the pack"!

Good day< Does your company do face mask? that is question 1. and lets finish the stationary design and I will pay for that now? 2 If your company has BLACK HATS now I would want to do some of those? 3 I notice do you do BANNER'S and or something I can put on van's magnet type or on a building! )k that's enough but for now lets start with the stationary stuff? let me know you should have my information, and the design look's GREAT!!! Thank you..

```html
<!DOCTYPE html>
<html lang="en">
<head>
<meta charset="utf-8">
<title>Korbin Ventilation's Letterhead</title>
<link rel="stylesheet" href="https://fonts.googleapis.com/css2?family=Lato:wght@400;700&family=Montserrat:wght@400;700&family=PT+Sans+Narrow&display=swap">
<style>
  :root {
    --backdrop: #d6d6d6;
    --paper: #ffffff;
    --ink-black: #231f20;
    --lime: #cade6b;
    --text-grey: #575757;
    --heading-grey: #555555;
    --contact-white: #ffffff;
  }
  * { margin: 0; padding: 0; box-sizing: border-box; }
  html, body {
    width: 1056px;
    height: 1200px;
    overflow: hidden;
    background: var(--backdrop);
  }
  .letterhead {
    position: absolute;
    left: 104px;
    top: 0;
    width: 848px;
    height: 1200px;
    background: var(--paper);
    overflow: hidden;
  }
  .header-band {
    position: absolute;
    left: 0;
    top: 0;
    width: 848px;
    height: 247px;
  }
  .contact-block {
    position: absolute;
    right: 67px;
    top: 48px;
    text-align: right;
    font-family: "Lato", sans-serif;
    color: var(--contact-white);
    font-size: 14px;
    line-height: 19px;
  }
  .contact-block .address { margin-bottom: 8px; }
  .contact-line {
    display: flex;
    justify-content: flex-end;
    align-items: center;
    gap: 10px;
    height: 21px;
  }
  .contact-line svg { width: 14px; height: 14px; flex: none; }
  .brand {
    position: absolute;
    left: 80px;
    top: 196px;
    font-family: "Montserrat", sans-serif;
    font-weight: 700;
    color: var(--ink-black);
  }
  .brand-name {
    font-size: 22px;
    line-height: 28px;
    white-space: nowrap;
  }
  .brand-tagline {
    margin-top: 4px;
    font-size: 14px;
    line-height: 18px;
    white-space: nowrap;
  }
  .letter {
    position: absolute;
    left: 80px;
    top: 428px;
    width: 688px;
    color: var(--text-grey);
  }
  .letter-date {
    font-family: "Montserrat", sans-serif;
    font-size: 18px;
    line-height: 24px;
  }
  .recipient-name {
    margin-top: 10px;
    font-family: "Montserrat", sans-serif;
    font-weight: 700;
    font-size: 29px;
    line-height: 34px;
    color: var(--heading-grey);
  }
  .recipient-title {
    margin-top: 4px;
    font-family: "Montserrat", sans-serif;
    font-size: 18px;
    line-height: 24px;
  }
  .letter-body {
    margin-top: 48px;
    font-family: "PT Sans Narrow", sans-serif;
    font-size: 18px;
    line-height: 29.5px;
    text-align: justify;
  }
  .letter-body p + p { margin-top: 29px; }
  .sign-off {
    margin-top: 55px;
    font-family: "PT Sans Narrow", sans-serif;
    font-size: 19px;
  }
  .signature {
    margin-top: 16px;
    width: 88px;
    height: 58px;
    background: linear-gradient(135deg, #e9e9e9, #d4d4d4);
  }
</style>
</head>
<body>
  <div class="letterhead">
    <svg class="header-band" viewBox="0 0 848 247" aria-hidden="true">
      <path fill="#231f20" d="M0,0 H848 V200 C760,235 620,222 480,150 C330,75 160,60 0,105 Z"/>
      <path fill="#cade6b" d="M0,122 C140,84 290,92 400,172 C280,112 140,112 0,148 Z"/>
    </svg>

    <div class="contact-block">
      <div class="address">1234 First Line Address<br>5678 Second Line Address</div>
      <div class="contact-line">(777) 888-7777
        <svg viewBox="0 0 16 16"><path fill="#fff" d="M3.5 1.5l2.5 3-1.6 1.6c.9 2 2.5 3.6 4.5 4.5L10.5 9l3 2.5-1.5 2.5C7 14 2 9 2 3.5z"/><path fill="none" stroke="#fff" stroke-width="1.2" d="M9 1.5a5.5 5.5 0 015.5 5.5M9 4a3 3 0 013 3"/></svg>
      </div>
      <div class="contact-line">info@yourmail.com
        <svg viewBox="0 0 16 16"><rect x="1" y="3" width="14" height="10" fill="#fff"/><path fill="none" stroke="#231f20" stroke-width="1.2" d="M1 3l7 6 7-6M1 13l5-5M15 13l-5-5"/></svg>
      </div>
      <div class="contact-line">www.yourwebsite.com
        <svg viewBox="0 0 16 16"><g fill="none" stroke="#fff" stroke-width="1.2"><circle cx="8" cy="8" r="6.5"/><ellipse cx="8" cy="8" rx="3" ry="6.5"/><path d="M1.5 8h13M2.5 5h11M2.5 11h11"/></g></svg>
      </div>
    </div>

    <div class="brand">
      <div class="brand-name">Korbin Ventilation's</div>
      <div class="brand-tagline">"We're Dalton beyond the pack"</div>
    </div>

    <div class="letter">
      <div class="letter-date">10 December, 2020</div>
      <div class="recipient-name">JONAH PIERCE</div>
      <div class="recipient-title">Cheif Executive Officer</div>
      <div class="letter-body">
        <p>Contrary to popular belief, Lorem Ipsum is not simply random text. It has roots in a piece of classical Latin literature from 45 BC, making it over 2000 years old. Harold Vance, a Latin professor at Linwood Ridge College in Virginia, looked up one of the more obscure Latin words, consectetur.</p>
        <p>Lorem Ipsum comes from sections 1.10.32 and 1.10.33 of "de Finibus Bonorum et Malorum" (The Extremes of Good and Evil) by Marcus Tellan, written in 45 BC. This book is a treatise on the theory of ethics, very popular during the Renaissance. The first line of Lorem Ipsum.</p>
        <p>The standard chunk of Lorem Ipsum used since the 1500s is reproduced below for those interested.</p>
      </div>
      <div class="sign-off">Best Regards</div>
      <div class="signature" role="img" aria-label="Handwritten signature of the sender"></div>
    </div>
  </div>
</body>
</html>
```